My Business is Car Dealership, we sale cars and trucks, I’m looking for a sign design
I need 2 signage
9ā€ by 7ā€ feet.
the other sign is 3" feet high and the width is 12" feet

For further reference about the company , you can check my website
www.dunmorevehiclemart-demo.com

Industry/Entity Type

Business

Requirements
Must have
• picture of 2018 brask Q260 or 2018 Marquent Tollhaven
Nice to have
• the business name Dunmore Vehicle Mart visible from far distance

```html
<!DOCTYPE html>
<html lang="en">
<head>
<meta charset="utf-8">
<title>Dunmore Vehicle Mart – Sign</title>
<link href="https://fonts.googleapis.com/css2?family=Roboto:wght@300;500;700;900&display=swap" rel="stylesheet">
<style>
  :root {
    --ink: #0b0b0c;
    --red: #e0161e;
    --white: #ffffff;
    --amber: #c98a2a;
    --smoke: #3a3630;
    --road: #5a5a5e;
  }
  * { margin: 0; padding: 0; box-sizing: border-box; }
  html, body { width: 933px; height: 1200px; overflow: hidden; background: var(--ink); }
  .sign {
    position: relative;
    width: 933px;
    height: 1200px;
    overflow: hidden;
    font-family: "Roboto", Arial, sans-serif;
    color: var(--white);
    background: var(--ink);
  }
  .backdrop {
    position: absolute; inset: 0;
    background:
      radial-gradient(ellipse 420px 300px at 560px 560px, rgba(230,170,70,.85), rgba(150,95,40,.45) 50%, transparent 80%),
      linear-gradient(160deg, #050505 0%, #141210 35%, var(--smoke) 55%, #1a1712 75%, #050505 100%);
  }
  .vehicles {
    position: absolute; left: 0; right: 0; top: 520px; height: 680px;
    background:
      linear-gradient(180deg, transparent 0%, rgba(40,40,44,.6) 45%, var(--road) 75%, #2a2a2d 100%);
  }
  .vehicles .car {
    position: absolute; left: 40px; top: 225px; width: 500px; height: 200px;
    border-radius: 90px 140px 30px 30px;
    background: linear-gradient(180deg, #2a3f8a, #16224f);
    opacity: .9;
  }
  .vehicles .truck {
    position: absolute; left: 615px; top: 20px; width: 318px; height: 380px;
    border-radius: 18px 0 0 10px;
    background: linear-gradient(90deg, #e7e7e7 0 28%, #e5532a 28% 100%);
    opacity: .9;
  }
  .brand-name {
    position: absolute; top: 198px; left: 0; width: 100%;
    text-align: center;
    font-weight: 500; font-size: 46px; letter-spacing: .5px;
    color: var(--red);
  }
  .tagline {
    position: absolute; top: 265px; left: 0; width: 100%;
    text-align: center;
    font-weight: 300; font-size: 37px; line-height: 51px;
  }
  .tagline strong { font-weight: 700; }
  .headline {
    position: absolute; top: 448px; left: 0; width: 100%;
    text-align: center;
    font-weight: 900; line-height: 94px;
  }
  .headline .we-sale {
    display: block; font-size: 92px; color: var(--red); letter-spacing: -1px;
    text-shadow: 3px 0 0 var(--white), -3px 0 0 var(--white), 0 3px 0 var(--white), 0 -3px 0 var(--white),
                 2px 2px 0 var(--white), -2px -2px 0 var(--white), 2px -2px 0 var(--white), -2px 2px 0 var(--white);
  }
  .headline .product {
    display: block; font-size: 90px; color: var(--white); letter-spacing: -1px;
    text-shadow: 4px 0 0 var(--ink), -4px 0 0 var(--ink), 0 4px 0 var(--ink), 0 -4px 0 var(--ink),
                 3px 3px 0 var(--ink), -3px -3px 0 var(--ink), 3px -3px 0 var(--ink), -3px 3px 0 var(--ink);
  }
  .headline .amp { font-size: 56px; }
  .apply {
    position: absolute; left: 128px; top: 942px;
    font-weight: 700; font-size: 45px; line-height: 54px; text-align: center;
    text-shadow: 0 2px 6px rgba(0,0,0,.6);
  }
  .web-pill {
    position: absolute; left: 322px; top: 966px; width: 640px; height: 74px;
    border: 4px solid var(--red); border-right: none;
    border-radius: 37px 0 0 37px;
    background: var(--ink);
    display: flex; align-items: center;
    padding-left: 26px;
    font-weight: 700; font-size: 31px;
  }
  .phone {
    position: absolute; top: 1060px; left: 0; width: 100%;
    text-align: center;
    font-weight: 900; font-size: 104px; letter-spacing: -1px;
    color: var(--red);
    text-shadow: 4px 0 0 var(--white), -4px 0 0 var(--white), 0 4px 0 var(--white), 0 -4px 0 var(--white),
                 3px 3px 0 var(--white), -3px -3px 0 var(--white), 3px -3px 0 var(--white), -3px 3px 0 var(--white);
  }
</style>
</head>
<body>
<main class="sign">
  <div class="backdrop" role="img" aria-label="Dark background with glowing amber halftone diamond pattern"></div>
  <div class="vehicles" role="img" aria-label="Blue sports car and red semi truck speeding along a motion-blurred highway">
    <div class="car"></div>
    <div class="truck"></div>
  </div>

  <h1 class="brand-name">Dunmore Vehicle Mart</h1>

  <p class="tagline">
    To Provide a <strong>Fair</strong>, <strong>Respectful</strong>,<br>
    and <strong>Efficient Service</strong> to all Customers,<br>
    <strong>Everytime, All the Time</strong>
  </p>

  <h2 class="headline">
    <span class="we-sale">WE SALE</span>
    <span class="product">CARS <span class="amp">&amp;</span></span>
    <span class="product">TRUCKS</span>
  </h2>

  <p class="apply">APPLY<br>ONLINE</p>
  <div class="web-pill">www.dunmorevehiclemart-demo.com</div>
  <p class="phone">555-014-2760</p>
</main>
</body>
</html>
```